meditation/yoga retreat eco village ashram commune website

There is a group of 20-30 people living in the jungle of mexico. We all came together from all walks of life to help built a paradise on earth. This is a meditation ashram resort that is built by a living enlightenment master, a modern day buddha master Swami Devakar Lunel. It's his vision and his love that he wants to share to the world.

The eco village project is on a 19 hectares forest land with a cenote (natural pond) as the heart centre surrounded by beautiful tropical gardens. This unique village is conceived in a mystical mayan circle as an oasis for creative arts crafts music and dance, mayan wisdom, eastern ayurveda, yoga, vipassana, meditation and silent retreat for the science of inner transformation this eco development will offer residents and visitors the experience of nature, silence, tranquility, meditativeness and a compassionate space for growth and flowering of human consciousness.

we are creating an inner science mystery school where we will offer ancient mayan traditions, buddhist vipassana, tibetan teachings, yoga, patanjali yoga, pranayama, we will also offer meditations and therapies like mystic rose, born again, no mind, painting group, breath, prana healing, primal, work as meditation all therapies and meditations will be offered for free we accept donations out of gratitude

The NEW DOMAIN for this website will be - www.LUNELTIKAL.example

This is our old website - http://luneldevakar.example/o/tikal/
it is outdated and we haven't done anything to it in the past 5 years. Now that we are about to open to the world, we want a fresh new look that will captivate our audience. Please take a moment to browse our website to get an idea of who we are.

Also please check out our facebook page, you will see all our past events, upcoming events with pics and videos.
www.facebook.example/luneltikal
www.instagram.example/luneltikal

We have 3 festivals coming up, they are as follows.
Yoga festival - https://www.facebook.example/events/4402918837165530/
Art festival - https://www.facebook.example/events/4409357162093341/
Thai massage - https://www.facebook.example/events/8835461290057213/

Do not use any of the pictures from the old website, it is outdated, most are just drawings and sketches. I have zipped up some great pictures for you to use, ...also feel free to use anything from facebook/instagram as well.

For menu, also we will have sub-categories menu for each as well.

HOME
NEWS
THE PROJECT
EVENTS
VIDEOS
PHOTOS
TICKETS
RESIDENTIAL
DONATE
CONTACT

Things to include for main page.
*Upcoming Events
*Previous Pics/Videos of Past Events (grab them from our facebook page)
*Show some great construction building, reed pavilion, fern pavilion, welcome center, etc..
*Maybe a section where the master can say a message.
*Mediation/Yoga section
*Residential Booking
*Facebook page, *twitter feed, instagram, youtube channel

Target Market(s)

meditation, yoga, art, dance festivals

Industry/Entity Type

Group

Number of Pages Required

1 page

Requirements
Must have
• we are looking for something classy, elegant, yet simple...stay away from traditional, give it a really cool modern touch.

```html
<!DOCTYPE html>
<html lang="en">
<head>
<meta charset="utf-8">
<title>Luneldevakar — Yoga Retreat Ashram</title>
<link href="https://fonts.googleapis.com/css2?family=Open+Sans:wght@400;600;700&family=Comfortaa:wght@400;700&display=swap" rel="stylesheet">
<style>
:root{
  --red:#d3151b;
  --red-dark:#9e0e12;
  --bg:#1b1b1b;
  --bg-dark:#121212;
  --bg-mid:#242424;
  --text:#d6d6d6;
  --muted:#9a9a9a;
  --white:#ffffff;
  --field:#2e2e2e;
}
*{margin:0;padding:0;box-sizing:border-box}
html,body{width:1200px;height:3724px;overflow:hidden}
body{background:var(--bg);color:var(--text);font-family:"Open Sans",Arial,sans-serif;font-size:13px;line-height:1.6;position:relative}
.section{position:absolute;left:0;width:1200px}
.red-rule{position:absolute;left:0;width:1200px;height:4px;background:var(--red)}
h2.section-title{color:var(--white);font-weight:600;font-size:24px;letter-spacing:1px;text-transform:uppercase;text-align:center}

/* header */
.site-header{position:absolute;top:0;left:0;width:1200px;height:130px;z-index:5}
.brand{position:absolute;left:40px;top:20px;display:flex;align-items:center;gap:12px;color:var(--white);font-weight:700;font-size:34px;letter-spacing:2px}
.brand .mark{width:26px;height:26px;background:var(--red)}
.topbar{position:absolute;right:90px;top:18px;display:flex;align-items:center;gap:14px}
.phone{color:var(--white);font-size:13px;font-weight:600;display:flex;align-items:center;gap:8px}
.phone .flag{width:22px;height:14px;background:#c7c7c7;border:1px solid #777}
.donate-btn{background:var(--red);color:var(--white);font-weight:700;font-size:13px;padding:6px 22px;letter-spacing:1px}
.social{display:flex;gap:8px}
.social span{width:28px;height:28px;border:2px solid #cfcfcf;border-radius:50%}
.main-nav{position:absolute;left:370px;top:92px;display:flex;font-size:14px}
.main-nav a{color:var(--white);text-decoration:none;padding:8px 12px}
.main-nav a.active{background:var(--red)}

/* hero */
.hero{top:0;height:660px;background:radial-gradient(ellipse at 50% 55%,#7a5a45 0%,#4a3a33 35%,#2a2322 70%,#161616 100%)}
.hero-band{position:absolute;left:120px;top:385px;width:960px;height:52px;background:linear-gradient(90deg,rgba(211,21,27,0),rgba(211,21,27,.9) 25%,rgba(211,21,27,.9) 75%,rgba(211,21,27,0));display:flex;align-items:center;justify-content:center}
.hero-band h1{color:var(--white);font-size:32px;font-weight:600;letter-spacing:2px}
.hero-text{position:absolute;left:300px;top:505px;width:600px;text-align:center;color:var(--white);font-size:14px}
.dots{position:absolute;top:612px;left:0;width:1200px;display:flex;justify-content:center;gap:10px}
.dots span{width:14px;height:14px;border-radius:50%;background:#e8e8e8}
.dots span.on{background:var(--red)}

/* welcome */
.welcome{top:664px;height:640px;background:var(--bg)}
.welcome h2{position:absolute;top:44px;left:0;width:1200px;font-family:"Comfortaa",sans-serif;font-weight:700}
.welcome h2 .initial{color:var(--red);font-size:34px}
.welcome .lead{position:absolute;top:130px;left:170px;width:860px;text-align:center;font-size:12px;color:var(--muted)}
.festival{position:absolute;top:250px;width:240px;text-align:center}
.festival .badge{width:240px;height:240px;border-radius:50%;border:6px solid #cfcfcf}
.festival h3{margin-top:24px;font-family:"Comfortaa",sans-serif;font-weight:400;font-size:24px;color:var(--white)}

/* past events */
.past{top:1308px;height:652px;background:var(--bg-mid)}
.video{position:absolute;left:108px;top:32px;width:492px;height:340px;background:linear-gradient(135deg,#3c3430,#6b5546 50%,#2b2420)}
.video .title{position:absolute;left:12px;top:8px;color:var(--white);font-size:13px;font-weight:600}
.video .play{position:absolute;left:216px;top:140px;width:60px;height:60px;border:3px solid var(--white);border-radius:50%}
.thumbs{position:absolute;left:108px;top:412px;display:flex;gap:20px}
.thumbs div{width:150px;height:150px;background:linear-gradient(135deg,#8a4a2a,#c28a56)}
.past-copy{position:absolute;left:650px;top:70px;width:440px}
.past-copy h2{color:var(--white);font-size:22px;font-weight:600;margin-bottom:18px}
.past-copy p{font-size:12px;color:var(--muted);margin-bottom:14px}
.btn-red{display:inline-block;background:var(--red);color:var(--white);font-weight:600;font-size:13px;padding:10px 26px;text-transform:uppercase}
.past-copy .btn-red{margin-top:6px}

/* master */
.master{top:1960px;height:420px;background:var(--bg-dark)}
.master-photo{position:absolute;left:600px;top:0;width:600px;height:420px;background:linear-gradient(180deg,#5b5f4c,#8a8f78 50%,#3d4033);clip-path:polygon(12% 0,100% 0,100% 100%,0 100%)}
.master .quote{position:absolute;left:108px;top:40px;color:var(--white);font-size:60px;font-weight:700;line-height:1}
.master h2{position:absolute;left:170px;top:52px;color:var(--white);font-size:22px;font-weight:600}
.master p{position:absolute;left:170px;top:110px;width:340px;font-size:12px;color:var(--muted);text-align:center}

/* meditation */
.meditation{top:2380px;height:560px;background:#161616}
.meditation h2{position:absolute;top:40px;left:0;width:1200px}
.meditation .sub{position:absolute;top:84px;left:200px;width:800px;text-align:center;font-size:12px;color:var(--muted)}
.grid{position:absolute;left:108px;top:130px;width:984px;display:grid;grid-template-columns:repeat(4,234px);grid-auto-rows:170px;gap:20px 16px}
.grid .tile{background:linear-gradient(135deg,#6e3a2a,#b26a3e)}
.grid .tile.cool{background:linear-gradient(135deg,#2a2f4e,#6a5a8a)}
.grid .tile.green{background:linear-gradient(135deg,#3a5a3a,#8aa06a)}
.grid .therapies{background:#3a3a3a;display:flex;align-items:center;justify-content:center;color:var(--white);font-size:22px}

/* booking */
.booking{top:2940px;height:280px;background:var(--bg-mid)}
.booking h2{position:absolute;left:108px;top:34px;color:var(--white);font-size:22px;font-weight:600;text-transform:uppercase}
.form{position:absolute;left:108px;top:88px;display:grid;grid-template-columns:230px 230px;gap:14px 20px}
.field{height:38px;background:var(--field);border:1px solid #555;color:#ccc;font-size:13px;padding:8px 12px;display:flex;justify-content:space-between}
.form .btn-red{text-align:center;padding:9px 0}
.booking-photo{position:absolute;left:740px;top:-10px;width:320px;height:320px;border-radius:50%;background:radial-gradient(circle,#9a9a9a,#4a4a4a 70%,#2a2a2a);border:6px solid #555}

/* footer */
.site-footer{top:3220px;height:452px;background:#151515}
.footer-brand{position:absolute;left:100px;top:40px;display:flex;align-items:center;gap:12px;color:var(--white);font-weight:700;font-size:40px;letter-spacing:2px}
.footer-brand .mark{width:30px;height:30px;background:var(--red)}
.footer-col{position:absolute;top:40px}
.footer-col h4{color:var(--white);font-size:15px;font-weight:700;text-transform:uppercase;margin-bottom:14px}
.footer-col li{list-style:none;font-size:13px;color:var(--text);line-height:1.9}
.footer-col li::before{content:"› ";color:var(--red)}
.contact-item{display:flex;gap:10px;margin-bottom:14px;font-size:12px}
.contact-item svg{flex:none;margin-top:3px}
.contact-item b{color:var(--white);display:block}
.tweet{margin-bottom:18px;font-size:12px}
.tweet b{color:var(--white)}
.tweet a{color:var(--red);text-decoration:none;word-break:break-all}
.footer-bar{position:absolute;top:3672px;left:0;width:1200px;height:52px;background:var(--red);color:var(--white);font-size:12px;display:flex;align-items:center;justify-content:space-between;padding:0 40px}
</style>
</head>
<body>

<section class="section hero">
  <div class="hero-band"><h1>YOGA RETREAT ASHRAM</h1></div>
  <p class="hero-text">This is a meditation ashram resort that is built by a living enlightenment master, a modern day buddha master Swami Devakar Lunel.</p>
  <div class="dots"><span class="on"></span><span></span><span></span><span></span><span></span></div>
</section>

<header class="site-header">
  <div class="brand"><span class="mark"></span>LUNEL</div>
  <div class="topbar">
    <div class="phone">0299-01234 <span class="flag"></span></div>
    <div class="donate-btn">DONATE</div>
    <div class="social"><span></span><span></span><span></span><span></span></div>
  </div>
  <nav class="main-nav">
    <a class="active">Home</a><a>News</a><a>The Project</a><a>Events</a><a>Videos</a><a>Photos</a><a>Tickets</a><a>Residential</a><a>Donate</a><a>Contact</a>
  </nav>
</header>

<div class="red-rule" style="top:660px"></div>

<section class="section welcome">
  <h2 class="section-title"><span class="initial">W</span>ELCOME TO LUNELDEVAKAR</h2>
  <p class="lead">This is a meditation ashram resort that is built by a living enlightenment master, a modern day buddha master Swami Devakar Lunel. It's his vision and his love that he wants to share to the world. The eco village project is on a 19 hectares forest land with a cenote (natural pond) as the heart centre surrounded by beautiful tropical gardens.</p>
  <div class="festival" style="left:160px"><div class="badge" role="img" aria-label="Yoga festival poster" style="background:radial-gradient(circle,#e8f0f0,#7ab8c8)"></div><h3>Yoga Festival</h3></div>
  <div class="festival" style="left:480px"><div class="badge" role="img" aria-label="Art festival poster" style="background:radial-gradient(circle,#d84a4a,#3a7a3a 70%)"></div><h3>Art festival</h3></div>
  <div class="festival" style="left:800px"><div class="badge" role="img" aria-label="Thai massage event poster" style="background:radial-gradient(circle,#8a5a8a,#2a2a3a)"></div><h3>Thai massage</h3></div>
</section>

<div class="red-rule" style="top:1304px"></div>

<section class="section past">
  <div class="video" role="img" aria-label="Video still of the master speaking">
    <span class="title">Dont Drop The Mind</span>
    <span class="play"></span>
  </div>
  <div class="thumbs">
    <div role="img" aria-label="Photo from a past festival"></div>
    <div role="img" aria-label="Photo of a group dance" style="background:linear-gradient(135deg,#5a3a2a,#a07050)"></div>
    <div role="img" aria-label="Photo of a ceremony" style="background:linear-gradient(135deg,#7a2a2a,#c46a4a)"></div>
  </div>
  <div class="past-copy">
    <h2>PICS/VIDEOS OF PAST EVENTS</h2>
    <p>This is a meditation ashram resort that is built by a living enlightenment master, a modern day buddha master Swami Devakar Lunel. It's his vision and his love that he wants to share to the world.</p>
    <p>The eco village project is on a 19 hectares forest land with a cenote (natural pond) as the heart centre surrounded by beautiful tropical gardens. This unique village is conceived in a mystical mayan circle as an oasis for creative arts crafts music and dance, mayan wisdom, eastern ayurveda, yoga, vipassana, meditation and silent retreat for the science of inner transformation.</p>
    <p>We are creating an inner science mystery school where we will offer ancient mayan traditions, buddhist vipassana, tibetan teachings, yoga, patanjali yoga, pranayama.</p>
    <span class="btn-red">View more</span>
  </div>
</section>

<section class="section master">
  <div class="master-photo" role="img" aria-label="White buddha statue in a tropical garden"></div>
  <div class="quote">“</div>
  <h2>MESSAGE FROM MASTER</h2>
  <p>inner science mystery school &amp; training courses<br>we are creating an inner science mystery school where we will offer ancient mayan traditions, buddhist vipassana, tibetan teachings, indian ayurveda, yoga, patanjali yoga, pranayama, healing, we will also offer meditations and therapies like mystic rose, born again, no mind, painting group, breath, prana healing, primal, work as meditation<br>all therapies and meditations will be offered for free<br>we accept donations out of gratitude</p>
</section>

<section class="section meditation">
  <h2 class="section-title">MEDITATION/YOGA SECTION</h2>
  <p class="sub">various methods of meditation like vipassana, zazen, kundalini, nadabrahma, dynamic, gourishankar, devavani, no mind, mandala, whirling and mystic rose for inner transformation</p>
  <div class="grid">
    <div class="tile" role="img" aria-label="Group meditating outdoors"></div>
    <div class="therapies">Meditative Therapies</div>
    <div class="tile green" role="img" aria-label="Yoga practice in the garden"></div>
    <div class="tile" role="img" aria-label="Evening dance meditation"></div>
    <div class="tile" role="img" aria-label="Celebration in orange robes"></div>
    <div class="tile green" role="img" aria-label="Meditation under the trees"></div>
    <div class="tile cool" role="img" aria-label="Night dance with lights"></div>
    <div class="tile green" role="img" aria-label="Portrait of a meditator"></div>
  </div>
</section>

<section class="section booking">
  <h2>Residential Booking:</h2>
  <div class="form">
    <div class="field">Name</div>
    <div class="field">Email</div>
    <div class="field">Phone Number</div>
    <div class="field">Select Date <span>▾</span></div>
    <div class="field">Select Time <span>▾</span></div>
    <div class="btn-red">Book Now</div>
  </div>
  <div class="booking-photo" role="img" aria-label="Reed pavilion residence seen from the garden"></div>
</section>

<footer class="section site-footer">
  <div class="footer-brand"><span class="mark"></span>LUNEL</div>
  <div class="footer-col" style="left:440px">
    <h4>Quick Links</h4>
    <ul><li>Home</li><li>News</li><li>The Project</li><li>Events</li><li>Videos</li><li>Residential</li><li>Contact Us</li></ul>
  </div>
  <div class="footer-col" style="left:620px;width:180px">
    <h4>Contact Us</h4>
    <div class="contact-item"><svg width="12" height="16" viewBox="0 0 12 16"><path d="M6 0a6 6 0 0 0-6 6c0 4.5 6 10 6 10s6-5.5 6-10a6 6 0 0 0-6-6zm0 8.5A2.5 2.5 0 1 1 6 3.5a2.5 2.5 0 0 1 0 5z" fill="#d3151b"/></svg><div><b>TIKAL GROVE</b>forest land, near the cenote, jungle road, Mexico</div></div>
    <div class="contact-item"><svg width="14" height="14" viewBox="0 0 14 14"><path d="M3 0l2 3-1.5 1.5a8 8 0 0 0 6 6L11 9l3 2-1.5 3C6 14 0 8 0 1.5z" fill="#d3151b"/></svg><div><b>PHONE</b>+0299-01234</div></div>
    <div class="contact-item"><svg width="14" height="10" viewBox="0 0 14 10"><rect width="14" height="10" fill="#d3151b"/><path d="M0 0l7 5 7-5" stroke="#151515" fill="none"/></svg><div><b>EMAIL</b>info@luneldevakar.example</div></div>
  </div>
  <div class="footer-col" style="left:840px;width:260px">
    <h4>Twitter Feed</h4>
    <div class="tweet"><b>@LUNELDEVAKAR</b><br>our new village project is on a 19 hectares forest land with a cenote at the heart<br><a>http://luneldevakar.example/o/tikal/</a></div>
    <div class="tweet"><b>@LUNELDEVAKAR</b><br>our new village project is on a 19 hectares forest land with a cenote at the heart<br><a>http://luneldevakar.example/o/tikal/</a></div>
  </div>
</footer>

<div class="footer-bar"><span>Copyright © 2016 Luneldevakar. All Rights Reserved</span><span>Link</span></div>

</body>
</html>
```